Mox Dune Reel Business cards

Logo, tag line and photo on card
Agent Name
Title
Address
Phone number
Email
Website
Make logo on one side large by rotating  to portrait format.  Keep the background of the logo white.

Contact Information for Business Card
Slogan; Shaping Every Mox Ahead

```html
<!DOCTYPE html>
<html lang="en">
<head>
<meta charset="utf-8">
<title>Mox Dune Reel – Business Cards</title>
<link href="https://fonts.googleapis.com/css2?family=Open+Sans:wght@400;600;700;800&display=swap" rel="stylesheet">
<style>
  :root {
    --navy: #22306a;
    --red: #c4232d;
    --white: #ffffff;
    --ink: #2b2b2b;
    --stage: #ece9e4;
    --photo-top: #8a8f96;
    --photo-bottom: #3c3f44;
  }
  * { box-sizing: border-box; margin: 0; padding: 0; }
  html, body {
    width: 1200px; height: 780px; overflow: hidden;
    background: var(--stage);
    font-family: "Open Sans", Arial, sans-serif;
  }
  .sheet {
    position: relative; width: 1200px; height: 780px;
    display: flex; justify-content: center; align-items: center; gap: 70px;
  }
  .card {
    position: relative; width: 380px; height: 640px;
    border-radius: 30px;
    box-shadow: 0 12px 30px rgba(0,0,0,.18);
    overflow: hidden;
  }
  .card--front { background: var(--white); }
  .card--back { background: var(--navy); }

  .agent-photo {
    position: absolute; top: 34px; right: 40px;
    width: 130px; height: 130px;
    background: linear-gradient(160deg, var(--photo-top), var(--photo-bottom));
  }
  .agent-details { position: absolute; top: 176px; left: 40px; right: 40px; }
  .agent-name {
    color: var(--red); font-weight: 700; font-size: 20px;
    letter-spacing: .5px; text-transform: uppercase; line-height: 1.15;
  }
  .agent-title { color: var(--ink); font-size: 13px; margin-top: 1px; }
  .contact-list { list-style: none; margin-top: 8px; }
  .contact-list li {
    display: flex; align-items: center; gap: 8px;
    color: var(--ink); font-size: 13px; line-height: 1.6;
  }
  .contact-list svg { width: 12px; height: 12px; flex: none; }
  .contact-address { color: var(--ink); font-size: 13px; line-height: 1.5; margin-top: 2px; }
  .brand-slogan {
    color: var(--navy); font-size: 12px; font-weight: 600;
    letter-spacing: .3px; margin-top: 6px;
  }

  .brand-frame {
    position: absolute; left: 34px; right: 34px; bottom: 30px; height: 228px;
    border: 7px solid var(--red); border-radius: 26px;
    display: flex; align-items: center; justify-content: center;
  }
  .card--back .brand-frame {
    top: 50%; bottom: auto; height: 330px; transform: translateY(-50%);
    border-color: var(--white);
  }
  .brand-name {
    color: var(--navy); font-weight: 800; font-size: 54px;
    line-height: 1.02; text-align: center; letter-spacing: -1px;
  }
  .card--back .brand-name { color: var(--white); font-size: 62px; }
</style>
</head>
<body>
<main class="sheet">
  <section class="card card--front" aria-label="Business card front">
    <div class="agent-photo" role="img" aria-label="Portrait photo of the agent"></div>
    <div class="agent-details">
      <h1 class="agent-name">Orin Vale</h1>
      <p class="agent-title">Managing Director</p>
      <ul class="contact-list">
        <li>
          <svg viewBox="0 0 16 16" aria-hidden="true"><path fill="var(--red)" d="M3.6 1.5l2.3 2.6-1.3 1.6c.9 2 2.4 3.5 4.4 4.5l1.6-1.3 2.6 2.3-1.5 2.3C6.3 13.2 2.8 9.7 1.3 4.3z"/></svg>
          123 456 789
        </li>
        <li>
          <svg viewBox="0 0 16 16" aria-hidden="true"><rect x="1" y="3" width="14" height="10" rx="1.5" fill="var(--red)"/><path d="M1.5 3.8L8 9l6.5-5.2" fill="none" stroke="#fff" stroke-width="1.4"/></svg>
          info@youremail.com
        </li>
        <li>
          <svg viewBox="0 0 16 16" aria-hidden="true"><circle cx="8" cy="8" r="7" fill="var(--red)"/><path d="M1.5 8h13M8 1c2.2 2 2.2 12 0 14M8 1c-2.2 2-2.2 12 0 14" fill="none" stroke="#fff" stroke-width="1"/></svg>
          www.yourwebsite.com
        </li>
      </ul>
      <p class="contact-address">Your address, City<br>State, Zip 1234</p>
      <p class="brand-slogan">Shaping Every Mox Ahead</p>
    </div>
    <div class="brand-frame">
      <p class="brand-name">Mox<br>Dune<br>Reel</p>
    </div>
  </section>

  <section class="card card--back" aria-label="Business card back">
    <div class="brand-frame">
      <p class="brand-name">Mox<br>Dune<br>Reel</p>
    </div>
  </section>
</main>
</body>
</html>
```